Stationery Design Project for Marketing Consultancy

I have started a new consultancy business and require the following elements to be designed using existing logo:
• Business card
• Letterhead
• Envelope (DL, C4, C5)
• Microsoft word template for report writing
• A4 Presentation Folder
• Powerpoint template
COPY FOR FRONT AND BACK OF BUSINESS CARD
logo
'Measurable Marketing. Epic Results' slogan (but no need to use existing lockup with logo)
name, B Com, Grad Cert Brand Strategy (post nominal abbreviations in smaller font)
mobile: 04XX-XXX-XXX (I will give details to the winner to add)
website: www.quorvial.com.au
email: info@quorvial.com.au
COPY FOR LETTERHEAD
Logo
Company Name
Please, submit your designs that include business card, letterhead and envelope. Once selected the winner will be asked to complete the project by creating the rest of the artwork.
FINAL FILES
Print ready files to be supplied as well as Indesign files so that minor amends can be made if necessary in future.
• Layered vectors in EPS & PDF
• Screen quality JPEG & PNGs
ABOUT THE BUSINESS: QUORVIAL
I work with clients to understand their business challenges, developing and executing measurable marketing strategies tied to key business metrics. Services include:
Services include:
• Business planning and business development
• Marketing and brand strategy
• Insight-driven integrated campaigns
• Loyalty programs and retention marketing
• Marketing automation
• Direct marketing (traditional and digital)
• Content strategy and development
Hi everyone,
Target Market(s)
Corporate decision makers (heads of marketing, general managers etc) and small to medium sized business owners. Predominately male aged 35+
Industry/Entity Type
Marketing
Requirements
Must have
- BRAND PERSONALITY
The successful design will communicate brand personality. I am a professional, results-driven entrepreneur, but want to show off my creative flair.
MEMORABILITY
Looking for a unique and eye-catching design. Am considering special printing effects (die cuts, letterpress, interactive elements, embossing, foiling etc) or a striking minimalist approach.
Nice to have
- I have a mission that could be incorporated on reverse if room -
Turning insights into actions & passion into profit.
Should not have
- Use of pink or green.

```html
<!DOCTYPE html>
<html lang="en">
<head>
<meta charset="utf-8">
<title>Quorvial Stationery</title>
<link href="https://fonts.googleapis.com/css2?family=Montserrat:wght@400;600;800&display=swap" rel="stylesheet">
<style>
  :root {
    --charcoal: #4a4a4c;
    --charcoal-dark: #3c3c3e;
    --gold: #d4ab0c;
    --paper: #f3f3f3;
    --ink: #1e1e1e;
    --backdrop: #ecebe8;
    --white: #ffffff;
  }
  * { margin: 0; padding: 0; box-sizing: border-box; }
  html, body { width: 1200px; height: 900px; overflow: hidden; }
  body {
    background: var(--backdrop);
    font-family: "Montserrat", sans-serif;
    position: relative;
  }
  .piece { position: absolute; overflow: hidden; box-shadow: 0 2px 8px rgba(0,0,0,.18); }

  .wordmark { font-weight: 800; letter-spacing: .02em; color: var(--ink); line-height: 1; white-space: nowrap; }
  .tagline { font-weight: 600; font-size: 6px; letter-spacing: .03em; color: var(--ink); margin-top: 3px; white-space: nowrap; }

  .corner-disc { position: absolute; border-radius: 50%; background: var(--gold); }
  .mark-dot { position: absolute; width: 16px; height: 16px; border-radius: 50%; background: var(--charcoal-dark); }

  .contact-strip {
    position: absolute; left: 18px; bottom: 20px;
    display: flex; align-items: center; gap: 8px;
    color: var(--white); font-size: 6px; white-space: nowrap;
  }
  .contact-strip .name { font-weight: 800; font-size: 10px; }

  /* DL envelope front */
  .envelope-front { left: 30px; top: 25px; width: 395px; height: 190px; background: var(--charcoal); }
  .envelope-front .brand { position: absolute; left: 24px; top: 18px; }
  .envelope-front .wordmark { font-size: 19px; }
  .envelope-front .corner-disc { width: 150px; height: 150px; right: -40px; bottom: -70px; }

  /* DL envelope back */
  .envelope-back { left: 32px; top: 247px; width: 395px; height: 187px; background: var(--gold); }
  .envelope-back .flap {
    position: absolute; left: 0; top: 0; width: 100%; height: 62px;
    background: var(--charcoal); clip-path: polygon(0 0, 100% 0, 100% 72%, 97% 100%, 3% 100%, 0 72%);
  }
  .envelope-back .mark-dot { right: 22px; bottom: 22px; }

  /* Letterhead */
  .letterhead { left: 453px; top: 32px; width: 350px; height: 495px; background: var(--paper); }
  .letterhead .brand { position: absolute; left: 18px; top: 17px; }
  .letterhead .wordmark { font-size: 20px; }
  .letterhead .footer-rule { position: absolute; left: 40px; right: 10px; bottom: 14px; height: 6px; background: var(--gold); }
  .letterhead .footer-rule::after { content: ""; position: absolute; right: 0; top: 0; width: 10px; height: 100%; background: var(--charcoal); }

  /* Letterhead reverse */
  .letterhead-back { left: 825px; top: 70px; width: 352px; height: 495px; background: var(--gold); }
  .letterhead-back .mark-dot { right: 22px; bottom: 22px; }

  /* Business card reverse */
  .card-back { left: 160px; top: 452px; width: 282px; height: 140px; background: var(--gold); border-radius: 14px; }
  .card-back .corner-disc { width: 112px; height: 112px; left: -46px; bottom: -52px; background: var(--charcoal); }
  .card-back .mark-dot { left: 190px; top: 36px; }

  /* Business card front */
  .card-front { left: 35px; top: 605px; width: 405px; height: 225px; background: var(--charcoal); border-radius: 16px; }
  .card-front .brand { position: absolute; left: 52px; top: 52px; }
  .card-front .wordmark { font-size: 24px; }
  .card-front .tagline { font-size: 8px; }
  .card-front .corner-disc { width: 170px; height: 170px; right: -70px; top: -60px; }
  .card-front .details { position: absolute; left: 72px; top: 100px; color: var(--white); }
  .details .name { font-weight: 800; font-size: 13px; white-space: nowrap; }
  .details .post-nominals { font-size: 7px; margin: 1px 0 6px; white-space: nowrap; }
  .details ul { list-style: none; font-size: 10px; line-height: 1.35; }
  .details li { display: flex; align-items: center; gap: 6px; white-space: nowrap; }
  .details svg { width: 9px; height: 9px; }

  /* Small card pair */
  .mini-front { left: 802px; top: 590px; width: 158px; height: 90px; background: var(--charcoal); }
  .mini-front .brand { position: absolute; left: 10px; top: 10px; }
  .mini-front .wordmark { font-size: 12px; }
  .mini-front .tagline { font-size: 4px; margin-top: 2px; }
  .mini-front .details { position: absolute; left: 10px; top: 38px; }
  .mini-front .details .name { font-size: 6px; }
  .mini-front .details .post-nominals { font-size: 3px; margin-bottom: 3px; }
  .mini-front .details ul { font-size: 4px; }
  .mini-front .corner-disc { width: 70px; height: 70px; right: -28px; bottom: -28px; }
  .mini-back { left: 983px; top: 618px; width: 170px; height: 90px; background: var(--gold); }
  .mini-back .corner-disc { width: 60px; height: 60px; left: -24px; bottom: -26px; background: var(--charcoal); }
  .mini-back .mark-dot { width: 10px; height: 10px; right: 34px; top: 38px; }
</style>
</head>
<body>

<section class="piece envelope-front">
  <div class="brand"><div class="wordmark">QUORVIAL</div><div class="tagline">CLEAR METRICS. BOLD OUTCOMES.</div></div>
  <div class="corner-disc"></div>
</section>

<section class="piece envelope-back">
  <div class="flap"></div>
  <div class="contact-strip">
    <span class="name">Callum Reyes</span><span>04XX-XXX-XXX</span><span>www.quorvial.com.au</span><span>info@quorvial.com.au</span>
  </div>
  <div class="mark-dot"></div>
</section>

<section class="piece letterhead">
  <div class="brand"><div class="wordmark">QUORVIAL</div><div class="tagline">CLEAR METRICS. BOLD OUTCOMES.</div></div>
  <div class="footer-rule"></div>
</section>

<section class="piece letterhead-back">
  <div class="contact-strip">
    <span class="name">Callum Reyes</span><span>04XX-XXX-XXX</span><span>www.quorvial.com.au</span><span>info@quorvial.com.au</span>
  </div>
  <div class="mark-dot"></div>
</section>

<section class="piece card-back">
  <div class="corner-disc"></div>
  <div class="mark-dot"></div>
</section>

<section class="piece card-front">
  <div class="brand"><div class="wordmark">QUORVIAL</div><div class="tagline">CLEAR METRICS. BOLD OUTCOMES.</div></div>
  <div class="details">
    <div class="name">Callum Reyes</div>
    <div class="post-nominals">B Com, Grad Cert Brand Strategy</div>
    <ul>
      <li><svg viewBox="0 0 10 10"><circle cx="5" cy="5" r="4.3" fill="none" stroke="#fff" stroke-width="1"/><path d="M3.4 3c.3 1.8 1.6 3.2 3.4 3.6" stroke="#fff" stroke-width="1" fill="none"/></svg>04XX-XXX-XXX</li>
      <li><svg viewBox="0 0 10 10"><circle cx="5" cy="5" r="4.3" fill="none" stroke="#fff" stroke-width="1"/><path d="M1 5h8M5 1c-2 2.5-2 5.5 0 8M5 1c2 2.5 2 5.5 0 8" stroke="#fff" stroke-width=".8" fill="none"/></svg>www.quorvial.com.au</li>
      <li><svg viewBox="0 0 10 10"><circle cx="5" cy="5" r="4.3" fill="none" stroke="#fff" stroke-width="1"/><path d="M3 3.5h4v3H3zM3 3.5l2 1.6 2-1.6" stroke="#fff" stroke-width=".8" fill="none"/></svg>info@quorvial.com.au</li>
    </ul>
  </div>
  <div class="corner-disc"></div>
</section>

<section class="piece mini-front">
  <div class="brand"><div class="wordmark">QUORVIAL</div><div class="tagline">CLEAR METRICS. BOLD OUTCOMES.</div></div>
  <div class="details">
    <div class="name">Callum Reyes</div>
    <div class="post-nominals">B Com, Grad Cert Brand Strategy</div>
    <ul><li>04XX-XXX-XXX</li><li>www.quorvial.com.au</li><li>info@quorvial.com.au</li></ul>
  </div>
  <div class="corner-disc"></div>
</section>

<section class="piece mini-back">
  <div class="corner-disc"></div>
  <div class="mark-dot"></div>
</section>

</body>
</html>
```